【 概要 】 IT系資格試験の過去問題を学習できるサイトで、 有料の会員(メンバー)に向けて、広告の非表示や、解説データの提供、追加機能などのサービスを提供しております。 サービスのトップページに掲載するバナー画像を募集します。 リンク先となるメンバーシップ紹介ページ https://www.sorairogakushu.com/membership/ 【 依頼内容 】 ・サイズ: 横1,280px × 縦200px(表示サイズはPC:横500px、縦80px、SP:横全幅) ・作成数: 1種類 ・利用用途:ウェブサイト ・掲載場所(現在は違うバナー画像が掲載されています) 【PC表示】https://www.sorairogakushu.com/hkrenshu.php 【SP 表示 】 https://www.sorairogakushu.com/s/hkrenshu.php 【 デザインイメージ 】 ・ターゲット層:20〜40代男性 ・雰囲気:サイトのイメージに合うスマートな印象、ごちゃごちゃしていない、"売り売り"していない ・上記掲載場所のサイトは水色メインの配色ですが、別の同じようなサイトでも使いたいのでどの配色にでも合うものだと嬉しいです。 ・金額の記載はなし 【 契約金額(税抜) 】 4,000円 ※契約金額(税込)からシステム利用料を差し引いた金額が、ワーカーさまの受取金額となります 。 ※本依頼に申込みをいただいた段階で、作成していただいたバナー画像の著作権は当方に譲渡するものとし、 作成していただくバナー画像について著作権人格権を行使しないことについて同意を得たとみなします。 その他ご質問等ありましたら、気軽にお問い合わせください。 いただいた提案が多い場合には、個別に返信できかねる場合がございますのでご了承くださいませ。 ご応募をお待ちしております! |
実際のサイト上に合わせてみたところマッチしていて、私の好みのイメージでもありました。また、利用者の合格をイメージさせるデザインが大変よく採用に至りました。サイト名が入っていないので他のサイトへの表示が編集なく行えることもポイントでした。
皆さま、この度はお時間を使ってご提案くださり誠にありがとうございました。いただいたメッセージに個々に返信することができず申し訳ございません。
本当に素晴らしいデザインが多く、また非常にたくさんのご提案をいただいたので決めるのが大変という嬉しい悲鳴でした。
今後もバナー等デザインのお仕事をするときにはこちらに依頼させていただこうと思います。

```html
<!DOCTYPE html>
<html lang="ja">
<head>
<meta charset="utf-8">
<title>そらいろ学習ドットコム パートナーシップ制度</title>
<link rel="stylesheet" href="https://fonts.googleapis.com/css2?family=Noto+Sans+JP:wght@700;900&display=swap">
<style>
  :root {
    --bg-dark: #1c1d20;
    --bg-mid: #3a3c40;
    --text-light: #ffffff;
    --accent: #e8501d;
    --accent-deep: #c83d10;
  }
  html, body {
    margin: 0;
    padding: 0;
    width: 1200px;
    height: 188px;
    overflow: hidden;
    background: var(--bg-dark);
  }
  .banner {
    position: relative;
    width: 1200px;
    height: 188px;
    overflow: hidden;
    font-family: "Noto Sans JP", sans-serif;
    color: var(--text-light);
  }
  .banner__photo {
    position: absolute;
    inset: 0;
    background:
      radial-gradient(ellipse at 75% 30%, rgba(120,122,128,0.45), transparent 60%),
      linear-gradient(100deg, var(--bg-dark) 0%, #2a2b2f 40%, var(--bg-mid) 75%, #2c2d31 100%);
  }
  .banner__shade {
    position: absolute;
    inset: 0;
    background: linear-gradient(90deg, rgba(10,10,12,0.55) 0%, rgba(10,10,12,0.15) 70%, rgba(10,10,12,0) 100%);
  }
  .banner__accent {
    position: absolute;
    left: 0;
    top: 0;
  }
  .banner__title {
    position: absolute;
    left: 60px;
    top: 14px;
    margin: 0;
    font-weight: 900;
    font-size: 62px;
    line-height: 1.2;
    letter-spacing: 1px;
    white-space: nowrap;
  }
  .banner__subtitle {
    position: absolute;
    left: 62px;
    top: 106px;
    margin: 0;
    font-weight: 700;
    font-size: 46px;
    line-height: 1.2;
    letter-spacing: 1px;
    white-space: nowrap;
  }
  .cta {
    position: absolute;
    right: 0;
    bottom: 14px;
    width: 330px;
    height: 70px;
  }
  .cta__label {
    position: absolute;
    left: 32px;
    top: 6px;
    font-weight: 900;
    font-size: 34px;
    line-height: 1.2;
    white-space: nowrap;
  }
  .cta__bar {
    position: absolute;
    left: 0;
    right: 0;
    bottom: 0;
    height: 10px;
    background: var(--accent);
  }
  .cta__icon {
    position: absolute;
    right: 8px;
    top: 2px;
  }
</style>
</head>
<body>
  <div class="banner">
    <div class="banner__photo" role="img" aria-label="暗いトーンのキーボードと眼鏡の写真"></div>
    <div class="banner__shade"></div>

    <svg class="banner__accent" width="40" height="188" viewBox="0 0 40 188" aria-hidden="true">
      <polygon points="0,0 18,0 0,120" fill="var(--accent)"/>
    </svg>

    <h1 class="banner__title">IT そらいろ学習ドットコム</h1>
    <p class="banner__subtitle">パートナーシップ制度</p>

    <a class="cta" aria-label="詳しくはこちら">
      <span class="cta__label">詳しくはこちら</span>
      <svg class="cta__icon" width="54" height="54" viewBox="0 0 54 54" aria-hidden="true">
        <circle cx="27" cy="27" r="26" fill="var(--accent)"/>
        <path d="M20 15 L20 38 L26 32 L30 41 L34 39 L30 30 L38 30 Z" fill="var(--text-light)"/>
      </svg>
      <span class="cta__bar"></span>
    </a>
  </div>
</body>
</html>
```